Business Card Design

Quiet Meadows - edgy, unique, ontrend clothing for girls 0-12.
I would like simple styling with white background and natural beige/brown font, similar to attached font.

Industry/Entity Type

Clothing

Contact Information for Business Card

Hi, I would like a very simple business card, white background with natural, beige, brown font, Quiet Meadows. I design and sell clothes for girls 0-12 with a touch of bohemian styling. I would like "Quiet Meadows" on front and on back -
www.quietmeadows-example.com.au
Delia Hartwell,
0481552937,
deliahartwell@brightnest-mail.com.au

```html
<!DOCTYPE html>
<html lang="en">
<head>
<meta charset="utf-8">
<title>Quiet Meadows – Business Card</title>
<link rel="stylesheet" href="https://fonts.googleapis.com/css2?family=Pinyon+Script&display=swap">
<style>
  :root {
    --backdrop: #2c313b;
    --card-corner: #8f7559;
    --card-cream: #f1e9d2;
    --card-cream-deep: #e6dbbd;
    --ribbon: #ec9d85;
    --ribbon-light: #f3b6a3;
    --ribbon-edge: #d98770;
    --ink-brown: #4e2e22;
  }
  html, body {
    margin: 0;
    width: 1200px;
    height: 1000px;
    overflow: hidden;
    background: var(--backdrop);
  }
  .canvas {
    position: relative;
    width: 1200px;
    height: 1000px;
  }
  .card {
    position: absolute;
    left: 240px;
    width: 720px;
    height: 400px;
  }
  .card--back { top: 60px; }
  .card--front { top: 530px; }
  .card svg { display: block; width: 720px; height: 400px; }
  .script {
    font-family: "Pinyon Script", cursive;
    fill: var(--ink-brown);
  }
</style>
</head>
<body>
<main class="canvas">

  <!-- Back: contact side -->
  <section class="card card--back" aria-label="Business card, contact side">
    <svg viewBox="0 0 720 400" xmlns="http://www.w3.org/2000/svg">
      <defs>
        <linearGradient id="creamBack" x1="0" y1="0" x2="1" y2="1">
          <stop offset="0" stop-color="var(--card-cream)"/>
          <stop offset="1" stop-color="var(--card-cream-deep)"/>
        </linearGradient>
        <linearGradient id="ribbonBack" x1="0" y1="0" x2="0" y2="1">
          <stop offset="0" stop-color="var(--ribbon-light)"/>
          <stop offset="1" stop-color="var(--ribbon-edge)"/>
        </linearGradient>
      </defs>
      <rect class="card-corner" width="720" height="400" fill="var(--card-corner)"/>
      <rect class="card-face" role="img" aria-label="Cream card face with a quilted diamond pattern"
            width="720" height="400" rx="22" fill="url(#creamBack)"/>
      <polygon class="ribbon-band" points="0,346 720,186 720,216 0,376" fill="url(#ribbonBack)"/>
      <text class="script contact-name" x="340" y="92" text-anchor="middle" font-size="54">Delia Hartwell</text>
      <text class="script contact-web" x="340" y="140" text-anchor="middle" font-size="25">www.quietmeadows-example.com.au</text>
      <text class="script contact-phone" x="340" y="174" text-anchor="middle" font-size="25">mob: 0481552937</text>
      <text class="script contact-email" x="340" y="208" text-anchor="middle" font-size="25">deliahartwell@brightnest-mail.com.au</text>
    </svg>
  </section>

  <!-- Front: brand side -->
  <section class="card card--front" aria-label="Business card, brand side">
    <svg viewBox="0 0 720 400" xmlns="http://www.w3.org/2000/svg">
      <defs>
        <linearGradient id="creamFront" x1="0" y1="0" x2="1" y2="1">
          <stop offset="0" stop-color="var(--card-cream)"/>
          <stop offset="1" stop-color="var(--card-cream-deep)"/>
        </linearGradient>
        <linearGradient id="ribbonFront" x1="0" y1="0" x2="0" y2="1">
          <stop offset="0" stop-color="var(--ribbon-light)"/>
          <stop offset="1" stop-color="var(--ribbon-edge)"/>
        </linearGradient>
      </defs>
      <rect class="card-corner" width="720" height="400" fill="var(--card-corner)"/>
      <rect class="card-face" role="img" aria-label="Cream card face with a quilted diamond pattern"
            width="720" height="400" rx="22" fill="url(#creamFront)"/>
      <polygon class="ribbon-band" points="0,360 720,150 720,190 0,400" fill="url(#ribbonFront)"/>
      <rect class="ribbon-bow" role="img" aria-label="Satin ribbon bow"
            x="400" y="222" width="110" height="54" rx="14"
            fill="var(--ribbon)" transform="rotate(-16 455 249)"/>
      <text class="script brand-name" x="360" y="172" text-anchor="middle" font-size="64">Quiet Meadows</text>
    </svg>
  </section>

</main>
</body>
</html>
```